Changes to an existing brochure needed

We need to make some changed to an existing product brochure to add more localised information in it and to make it looks better.

We have set out in a pdf file where needs to be changed. Apart from that, any changes on the design of the brochure that can make the brochure looks better will be appreciated.

Target Market(s)

Technology market

Industry/Entity Type

Technology Equipment

Colors

Designer to choose colors to be used in the design.

Requirements
Must have
• The content outlined in the pdf file.
Nice to have
• Some creative designs that can make the brochure looks better and more professional.
Should not have
• N/A

```html
<!DOCTYPE html>
<html lang="en">
<head>
<meta charset="utf-8">
<title>Filament Range Brochure</title>
<link rel="stylesheet" href="https://fonts.googleapis.com/css2?family=Barlow:wght@400;500;700&family=Barlow+Semi+Condensed:wght@700&display=swap">
<style>
:root{
  --stage:#3a3a3a;
  --band-dark:#1b9238;
  --band-light:#3fb552;
  --green:#22a33e;
  --text-green:#1f9a37;
  --rule:#8fd19b;
  --halo:#e3f4e6;
  --white:#ffffff;
}
*{box-sizing:border-box;margin:0;padding:0}
html,body{width:1200px;height:480px;overflow:hidden;background:var(--stage)}
body{position:relative;font-family:"Barlow",Arial,sans-serif}
.band{position:absolute;left:50px;top:56px;width:1100px;height:368px;
  background:linear-gradient(100deg,var(--band-dark) 0%,var(--band-light) 55%,var(--band-dark) 100%)}
.panel{position:absolute;top:68px;width:345px;height:344px;background:var(--white);padding:8px 8px 0 10px}
.panel--materials{left:67px}
.panel--metals{left:428px}
.panel--specials{left:794px;padding-bottom:0}
.grid{display:grid;grid-template-columns:1fr 1fr;column-gap:6px}
.panel--materials .grid,.panel--metals .grid{grid-template-rows:repeat(5,66px)}
.panel--specials .grid{grid-template-rows:repeat(4,58px)}
.item{display:flex;align-items:center;gap:7px}
.photo{flex:none;width:58px;height:58px;border-radius:50%;
  border:3px solid var(--white);box-shadow:0 0 0 4px var(--halo),0 0 0 5px #c9ead0;
  background:radial-gradient(circle at 45% 40%,var(--tone-a),var(--tone-b))}
.panel--specials .photo{width:50px;height:50px}
.photo--empty{background:var(--white)}
.info{flex:1;align-self:stretch;display:flex;flex-direction:column;justify-content:flex-start;
  padding-top:8px;border-bottom:1px solid var(--rule);margin-bottom:4px}
.title{background:var(--green);color:var(--white);font:700 9.5px/11px "Barlow Semi Condensed",Arial,sans-serif;
  padding:0 6px;height:11px;white-space:nowrap;overflow:hidden}
.desc{color:var(--text-green);font-size:6.6px;line-height:1.3;font-weight:500;margin-top:4px}
.mini-table{display:grid;grid-template-columns:repeat(6,7px);gap:1px;margin-top:3px}
.mini-table span{height:4px;background:#cfe9d4;border:0.5px solid var(--green)}
.swatches{display:flex;gap:2px;margin-top:3px}
.swatch{width:22.5px;display:flex;flex-direction:column;align-items:center}
.swatch i{display:block;width:22px;height:17px;border-radius:2px;background:var(--c);border:0.5px solid #ddd}
.swatch b{font-weight:400;font-size:3.8px;color:#444;margin-top:1px;white-space:nowrap}
.footer{position:absolute;left:0;right:0;bottom:0;height:30px;background:var(--green);color:var(--white);
  font:700 7px/1.5 "Barlow Semi Condensed",Arial,sans-serif;padding:5px 10px}
</style>
</head>
<body>
<div class="band"></div>

<section class="panel panel--materials">
  <div class="grid">
    <article class="item"><div class="photo" role="img" aria-label="Printed rose model" style="--tone-a:#f6c7d0;--tone-b:#d8344f"></div><div class="info"><h3 class="title">PLA / PLA+</h3><p class="desc">• Environmental-friendly material.<br>• High print quality.<br>• Good strength.</p></div></article>
    <article class="item"><div class="photo" role="img" aria-label="Carbon fibre printed tools" style="--tone-a:#9a9a9a;--tone-b:#2d2d2d"></div><div class="info"><h3 class="title">vPA-CF</h3><p class="desc">20% carbon fibre.<br>Highly rigid. Good toughness<br>and wear-resistance.</p></div></article>
    <article class="item"><div class="photo" role="img" aria-label="Printed jet model" style="--tone-a:#e8e8e8;--tone-b:#3a3a3a"></div><div class="info"><h3 class="title">vABS Max</h3><p class="desc">Good temperature tolerance and<br>creep resistance. Flame retardant.</p></div></article>
    <article class="item"><div class="photo" role="img" aria-label="Printed low-poly figure" style="--tone-a:#6a6a6a;--tone-b:#151515"></div><div class="info"><h3 class="title">ABS / ABS+</h3><p class="desc">High strength.<br>Good toughness.<br>Low shrinkage for ABS+.</p></div></article>
    <article class="item"><div class="photo" role="img" aria-label="Printed translucent bells" style="--tone-a:#f4e37a;--tone-b:#d9263d"></div><div class="info"><h3 class="title">PETG</h3><p class="desc">Low shrinkage. Good toughness.<br>High transparency and gloss.</p></div></article>
    <article class="item"><div class="photo" role="img" aria-label="Printed car body" style="--tone-a:#8a8a8a;--tone-b:#1d1d1d"></div><div class="info"><h3 class="title">vASA</h3><p class="desc">Excellent mechanical property.<br>Outstanding UV-resistance.</p></div></article>
    <article class="item"><div class="photo" role="img" aria-label="Printed parts with support material" style="--tone-a:#f5f5f5;--tone-b:#d62630"></div><div class="info"><h3 class="title">PVA</h3><p class="desc">Water soluble material.<br>Ideal for support structure.</p><div class="mini-table"><span></span><span></span><span></span><span></span><span></span><span></span><span></span><span></span><span></span><span></span><span></span><span></span></div></div></article>
    <article class="item"><div class="photo" role="img" aria-label="Printed blue and white sculpture" style="--tone-a:#f2f2f2;--tone-b:#2f5fb0"></div><div class="info"><h3 class="title">HIPS</h3><p class="desc">Soluble in Limonence.<br>Works well with ABS</p></div></article>
    <article class="item"><div class="photo" role="img" aria-label="Printed clear vases" style="--tone-a:#ffffff;--tone-b:#d8c0c8"></div><div class="info"><h3 class="title">vPC</h3><p class="desc">High distortion temperature.<br>Low flammability.</p></div></article>
    <article class="item"><div class="photo" role="img" aria-label="Printed glowing lamp" style="--tone-a:#f7d24a;--tone-b:#1a1208"></div><div class="info"><h3 class="title">vPA (Nylon)</h3><p class="desc">High toughness.<br>Outstanding chemical<br>resistance.</p></div></article>
  </div>
</section>

<section class="panel panel--metals">
  <div class="grid">
    <article class="item"><div class="photo" role="img" aria-label="Copper-fill vase" style="--tone-a:#e0e0e0;--tone-b:#8a4a2a"></div><div class="info"><h3 class="title">vCopper</h3><p class="desc">Easy to process.<br>Metal texture after polishing.</p></div></article>
    <article class="item"><div class="photo" role="img" aria-label="Bronze-fill ingot model" style="--tone-a:#f1ecd4;--tone-b:#9a8a4a"></div><div class="info"><h3 class="title">Bronze</h3><p class="desc">Easy to print.<br>Nice shiny finish.</p></div></article>
    <article class="item"><div class="photo" role="img" aria-label="Aluminium-fill busts" style="--tone-a:#c8c8c8;--tone-b:#4a4a4a"></div><div class="info"><h3 class="title">vAl-fill</h3><p class="desc">Aluminium filled PLA filament.<br>Metal texture after polishing.</p></div></article>
    <article class="item"><div class="photo" role="img" aria-label="Steel-fill statue" style="--tone-a:#d8d8d8;--tone-b:#555555"></div><div class="info"><h3 class="title">vSteel</h3><p class="desc">Stainless steel filled PLA filament.<br>Metal texture after polishing.</p></div></article>
    <article class="item"><div class="photo" role="img" aria-label="Extruder cleaning filament" style="--tone-a:#e6f2f8;--tone-b:#2d6e8a"></div><div class="info"><h3 class="title">vClean</h3><p class="desc">Cleaning extruder before or<br>after prints. Wide printing<br>temperature range.</p></div></article>
    <article class="item"><div class="photo" role="img" aria-label="Colour changing printed vase outdoors" style="--tone-a:#f2a7c8;--tone-b:#3d7a2e"></div><div class="info"><h3 class="title">Color Change</h3><p class="desc">Color changing by UV or<br>temperature. Reversible<br>color change.</p></div></article>
    <article class="item"><div class="photo" role="img" aria-label="Wood-fill printed animal" style="--tone-a:#f1e4d2;--tone-b:#b89a7a"></div><div class="info"><h3 class="title">Wood</h3><p class="desc">Wood texture finish.<br>Low warping.</p></div></article>
    <article class="item"><div class="photo" role="img" aria-label="Bamboo-fill pagoda model" style="--tone-a:#f0e0d0;--tone-b:#9a4a2a"></div><div class="info"><h3 class="title">vBamboo</h3><p class="desc">Matte finish with dark bamboo<br>colour. Print with wood aroma.</p></div></article>
    <article class="item"><div class="photo" role="img" aria-label="Flexible printed shoe insole" style="--tone-a:#b8e07a;--tone-b:#2a6a8a"></div><div class="info"><h3 class="title">vFlex(TPU)/vElastic(TPE)</h3><p class="desc">High flexibility.<br>Good resilience.</p></div></article>
    <article class="item"><div class="photo" role="img" aria-label="Flexible printed part being bent" style="--tone-a:#ffffff;--tone-b:#b8b8b8"></div><div class="info"><h3 class="title">vTPU-98A</h3><p class="desc">Cost effective flexible material.<br>Good dimensional stability.</p></div></article>
  </div>
</section>

<section class="panel panel--specials">
  <div class="grid">
    <article class="item"><div class="photo" role="img" aria-label="Smooth printed golf ball" style="--tone-a:#ffffff;--tone-b:#d8d8d0"></div><div class="info"><h3 class="title">vSmooth</h3><p class="desc">Can be polished by alcohol.<br>Great material for metal casting.</p></div></article>
    <article class="item"><div class="photo" role="img" aria-label="Printed bird figures" style="--tone-a:#f4e24a;--tone-b:#d8d8d8"></div><div class="info"><h3 class="title">vMate (PCL)</h3><p class="desc">FDA approved material.<br>Low melting temperature.<br>Ideal for both 3D printer and 3D pen.</p></div></article>
    <article class="item"><div class="photo" role="img" aria-label="Red resin tower and ball" style="--tone-a:#f4a0a0;--tone-b:#d81e2a"></div><div class="info"><h3 class="title">vResin-PLA</h3><p class="desc">Environmental-friendly.<br>Solidified by both UV and<br>visible light.</p></div></article>
    <article class="item"><div class="photo" role="img" aria-label="Resin jewellery casting model" style="--tone-a:#e8e47a;--tone-b:#5a8a2a"></div><div class="info"><h3 class="title">vResin-JC</h3><p class="desc">High precision.<br>Smooth surface.<br>Ideal for metal casting.</p></div></article>
    <article class="item"><div class="photo" role="img" aria-label="Resin lattice model" style="--tone-a:#f2c890;--tone-b:#b8642a"></div><div class="info"><h3 class="title">vResin-NC</h3><p class="desc">Fast printing speed.<br>Low shrinkage</p></div></article>
    <article class="item"><div class="photo" role="img" aria-label="Dental resin model" style="--tone-a:#e8c8c0;--tone-b:#3a6a8a"></div><div class="info"><h3 class="title">vResin-DC</h3><p class="desc">Special designed for dental purpose.<br>High precision. Good hardness.</p></div></article>
    <article class="item"><div class="photo" role="img" aria-label="Printed boat model" style="--tone-a:#f4eee6;--tone-b:#c8b8a8"></div><div class="info"><h3 class="title">vPeek</h3><p class="desc">Outstanding mechanical<br>properties. High strength,<br>wear and fatigue resistance.</p></div></article>
    <article class="item"><div class="photo photo--empty"></div><div class="info"><h3 class="title">Stay tuned for more materials.</h3></div></article>
  </div>
  <div class="swatches">
    <div class="swatch"><i style="--c:#f4f4f4"></i><b>White</b></div>
    <div class="swatch"><i style="--c:#e6ead8"></i><b>Luminous Green</b></div>
    <div class="swatch"><i style="--c:#efe8dc"></i><b>Natural</b></div>
    <div class="swatch"><i style="--c:#f2c8b8"></i><b>Skin</b></div>
    <div class="swatch"><i style="--c:#f2e23a"></i><b>Yellow</b></div>
    <div class="swatch"><i style="--c:#e4b63a"></i><b>Gold</b></div>
    <div class="swatch"><i style="--c:#f28a2a"></i><b>Orange</b></div>
    <div class="swatch"><i style="--c:#f47a8a"></i><b>Luminous Red</b></div>
    <div class="swatch"><i style="--c:#c8d8e0"></i><b>Luminous Blue</b></div>
    <div class="swatch"><i style="--c:#f28ab8"></i><b>Pink</b></div>
    <div class="swatch"><i style="--c:#d8287a"></i><b>Magenta</b></div>
    <div class="swatch"><i style="--c:#d8202a"></i><b>Red</b></div>
    <div class="swatch"><i style="--c:#a8287a"></i><b>Glass Purple</b></div>
    <div class="swatch"><i style="--c:#e8d23a"></i><b>Glass Lemon</b></div>
  </div>
  <div class="swatches">
    <div class="swatch"><i style="--c:#e8a83a"></i><b>Glass Orange</b></div>
    <div class="swatch"><i style="--c:#b81e2a"></i><b>Glass Red</b></div>
    <div class="swatch"><i style="--c:#7a2a8a"></i><b>Purple</b></div>
    <div class="swatch"><i style="--c:#8a8a8a"></i><b>Gray</b></div>
    <div class="swatch"><i style="--c:#7ac85a"></i><b>Peak Green</b></div>
    <div class="swatch"><i style="--c:#7ab8e0"></i><b>Light Blue</b></div>
    <div class="swatch"><i style="--c:#2a7a4a"></i><b>Pine Green</b></div>
    <div class="swatch"><i style="--c:#2aa83a"></i><b>Green</b></div>
    <div class="swatch"><i style="--c:#2a4ab8"></i><b>Blue</b></div>
    <div class="swatch"><i style="--c:#3a6ad8"></i><b>Glass Light Blue</b></div>
    <div class="swatch"><i style="--c:#7a4a2a"></i><b>Brown</b></div>
    <div class="swatch"><i style="--c:#1a1a1a"></i><b>Black</b></div>
    <div class="swatch"><i style="--c:#c8c8c8"></i><b>Silver</b></div>
  </div>
  <div class="footer">
    <p>Multicolor Filament: PLA、PLA+、ABS、ABS+、PETG、HIPS、vMate、COLOR CHANGE、vResin Series......</p>
    <p>Please email sales@layerforge.com.au for more product information.</p>
  </div>
</section>
</body>
</html>
```